Real Estate Listing Signs for standard Yard arms

I need real estate listing signs done, for the standard sized sign to be hung beneath a white yard arm. To match existing logo. Information to be included:
-Logo
-Business name
-Phone number
-Marden Fosk Tundra Circle & Marden Fosk Realty logos (smaller print)

Colors to be Red and anywhere in the gray scale between black and white, or a combination of those.

Target Market(s)

Drive by visuals

Industry/Entity Type

Real Estate Agent

Colors

Designer to choose only greyscale colors for use in the design.

Requirements
Must have
• My Logo and business name in same/similar font to whats provided, the MF tundra circle logo (small on bottom or corner somewhere), My phone number, and a decent amount of red coloration on the sign.

```html
<!DOCTYPE html>
<html lang="en">
<head>
<meta charset="utf-8">
<title>Brannick Realty – Yard Arm Listing Sign</title>
<link href="https://fonts.googleapis.com/css2?family=Montserrat:wght@400;800&family=Oswald:wght@700&display=swap" rel="stylesheet">
<style>
  :root {
    --canvas: #e6e6e6;
    --frame: #111111;
    --panel: #f7f7f7;
    --panel-shade: #e4e4e4;
    --ink: #111111;
    --red: #e5121c;
    --contact-bg: #0c0c0c;
    --contact-text: #f2f2f2;
    --muted: #3a3a3a;
  }
  html, body {
    margin: 0;
    padding: 0;
    width: 1200px;
    height: 905px;
    overflow: hidden;
    background: var(--canvas);
  }
  .sign {
    position: absolute;
    left: 290px;
    top: 18px;
    width: 620px;
    height: 870px;
    background: var(--frame);
    border-radius: 4px;
  }
  .sign-face {
    position: absolute;
    left: 50px;
    top: 48px;
    width: 520px;
    height: 775px;
    background: linear-gradient(90deg, var(--panel-shade) 0%, var(--panel) 45%, var(--panel) 100%);
  }
  .brand-mark {
    position: absolute;
    top: 110px;
    left: 0;
    width: 100%;
    display: flex;
    justify-content: center;
    align-items: center;
    gap: 18px;
  }
  .brand-mark__square {
    width: 64px;
    height: 64px;
    background: var(--red);
  }
  .brand-mark__name {
    font-family: "Montserrat", sans-serif;
    font-weight: 800;
    font-size: 40px;
    color: var(--red);
    letter-spacing: 1px;
  }
  .business-name {
    position: absolute;
    top: 290px;
    left: 0;
    width: 100%;
    margin: 0;
    text-align: center;
    font-family: "Montserrat", sans-serif;
    font-weight: 800;
    font-size: 66px;
    line-height: 90px;
    color: var(--ink);
    letter-spacing: 1px;
  }
  .contact-box {
    position: absolute;
    left: 34px;
    top: 501px;
    width: 439px;
    height: 143px;
    background: var(--contact-bg);
    border-radius: 12px;
    text-align: center;
  }
  .contact-box__phone {
    display: block;
    margin-top: 14px;
    font-family: "Oswald", sans-serif;
    font-weight: 700;
    font-size: 64px;
    line-height: 72px;
    color: var(--red);
  }
  .contact-box__web {
    display: block;
    font-family: "Montserrat", sans-serif;
    font-weight: 400;
    font-size: 32px;
    line-height: 40px;
    color: var(--contact-text);
    letter-spacing: 1px;
  }
  .affiliate {
    position: absolute;
    left: 130px;
    top: 672px;
    font-family: "Montserrat", sans-serif;
    font-weight: 400;
    color: var(--muted);
  }
  .affiliate__group {
    display: block;
    font-size: 27px;
    line-height: 32px;
  }
  .affiliate__realty {
    display: block;
    font-size: 13px;
    line-height: 18px;
    letter-spacing: 1px;
  }
</style>
</head>
<body>
  <div class="sign">
    <div class="sign-face">
      <div class="brand-mark">
        <span class="brand-mark__square"></span>
        <span class="brand-mark__name">BRANNICK</span>
      </div>
      <h1 class="business-name">BRANNICK<br>REALTY</h1>
      <div class="contact-box">
        <span class="contact-box__phone">(555)-214-7730</span>
        <span class="contact-box__web">BRANNICKREALTY.COM</span>
      </div>
      <div class="affiliate">
        <span class="affiliate__group">MF TUNDRA CIRCLE</span>
        <span class="affiliate__realty">MARDEN FOSK REALTY</span>
      </div>
    </div>
  </div>
</body>
</html>
```